Registry Program Flyer design 2 - MV Linkway registry

We need two different flyers that will be distributed via web, email and print. This project is for the second of the two flyers.

The audience is patients and family members of patients with a specific disease. The flyer will be used to make patients aware of our web-based registry programs, and to inform/encourage patients to join.

An example prototype flyer with the text that should be used is attached. We would like to improve the design and layout of the flyer, while retaining as much of the language as appropriate.

The MVLinkway flyer should use the logo provided in the example and a color scheme compatible with the logo. The flyer may use the pictures included in the prototype.

If possible, a final format that allows us to edit the text is preferred. If this is not possible, we will finalize the text after receiving a prototype. Changes to the text will likely be minor.

Note: The design of the flyers for this project and the other project (Registry Program Flyer Design 1 - TRBQ registry) can be similar in style, however, they should not be duplicates.

Deliverables will be a final .PSD (photoshop) file with layers so we can edit text if necessary.

Target Market(s)

Physicians and healthcare professionals.

Requirements
Must have
• Use the attached logo and colors.

```html
<!DOCTYPE html>
<html lang="en">
<head>
<meta charset="utf-8">
<title>MV Linkway Registry Flyer</title>
<link rel="stylesheet" href="https://fonts.googleapis.com/css2?family=Open+Sans:wght@400;600;700;800&family=Playfair+Display:ital,wght@1,400&display=swap">
<style>
  :root {
    --page-bg: #e6e6e6;
    --flyer-black: #0d0d0d;
    --header-grey: #2b2b2b;
    --brand-red: #d7141c;
    --panel-bg: #1e1e1e;
    --panel-edge: #b9b2a4;
    --text-light: #f2f2f2;
    --text-muted: #d8d8d8;
    --white: #ffffff;
    --ink: #1a1a1a;
  }
  * { box-sizing: border-box; margin: 0; padding: 0; }
  html, body { width: 1200px; height: 900px; overflow: hidden; }
  body {
    background: var(--page-bg);
    font-family: "Open Sans", Arial, sans-serif;
    position: relative;
  }
  .flyer {
    position: absolute;
    left: 270px; top: 25px;
    width: 660px; height: 850px;
    background: var(--flyer-black);
    overflow: hidden;
    box-shadow: 0 6px 20px rgba(0,0,0,.25);
  }
  .flyer-header {
    position: absolute; left: 0; top: 0; width: 100%; height: 200px;
    background: linear-gradient(180deg, var(--header-grey) 0%, #151515 45%, var(--flyer-black) 100%);
  }
  .rule-top {
    position: absolute; left: 40px; right: 0; top: 30px; height: 3px;
    background: var(--brand-red);
  }
  .rule-band {
    position: absolute; left: 0; right: 0; top: 194px; height: 5px;
    background: var(--brand-red);
  }
  .brand-box {
    position: absolute; left: 45px; top: 38px; width: 169px; height: 44px;
    background: var(--white);
    display: flex; align-items: center; gap: 8px; padding-left: 10px;
  }
  .brand-mark { width: 16px; height: 16px; background: var(--brand-red); }
  .brand-name { font-size: 16px; font-weight: 600; color: var(--ink); }
  .headline-join {
    position: absolute; left: 25px; top: 122px;
    color: var(--white); white-space: nowrap; font-weight: 400;
  }
  .headline-join .script {
    font-family: "Playfair Display", Georgia, serif; font-style: italic; font-size: 21px;
  }
  .headline-join .site { font-size: 23px; font-weight: 700; }
  .photo {
    position: absolute; top: 96px; height: 85px;
    border: 4px solid var(--white); border-radius: 5px;
  }
  .photo-group { left: 355px; width: 144px; background: linear-gradient(180deg, #8aa2b4, #c9bfb0); }
  .photo-beach { left: 507px; width: 133px; background: linear-gradient(180deg, #a9c2d3, #8d7f6b); }
  .info-panel {
    position: absolute; left: 24px; top: 248px; width: 612px; height: 590px;
    border: 2px solid var(--panel-edge); border-radius: 40px;
    background: linear-gradient(180deg, #262626, var(--panel-bg));
  }
  .column { position: absolute; top: 20px; color: var(--text-light); font-size: 9.5px; line-height: 1.3; }
  .column-left { left: 30px; width: 270px; }
  .column-right { left: 324px; width: 262px; }
  .section-title { font-size: 12px; font-weight: 700; margin-bottom: 8px; }
  .section-title.large { font-size: 16px; margin-bottom: 7px; }
  .column p { text-align: justify; margin-bottom: 10px; color: var(--text-muted); }
  .audience-list { list-style: none; margin-bottom: 12px; }
  .audience-list li { display: flex; align-items: center; gap: 9px; margin-bottom: 2px; color: var(--text-muted); }
  .audience-list li::before {
    content: ""; width: 8px; height: 8px; border-radius: 50%;
    background: var(--brand-red); flex: none;
  }
  .benefit-list { list-style: none; margin: 0 0 12px 4px; }
  .benefit-list li { display: flex; gap: 9px; margin-bottom: 3px; color: var(--text-muted); }
  .benefit-list svg { flex: none; margin-top: 2px; }
  .closing-line {
    position: absolute; left: 0; width: 100%; top: 690px;
    text-align: center; color: var(--white);
    font-size: 16px; font-weight: 700; line-height: 1.3;
  }
  .partner-strip {
    position: absolute; left: 145px; top: 742px; width: 375px; height: 48px;
    background: var(--white);
    display: flex; align-items: center; justify-content: space-between; padding: 0 10px;
  }
  .partner-name { display: flex; align-items: center; gap: 5px; font-size: 10px; font-weight: 600; color: var(--ink); width: 95px; line-height: 1.1; }
  .partner-name .mark { width: 10px; height: 10px; background: var(--brand-red); flex: none; }
  .badge-round { width: 32px; height: 32px; border-radius: 50%; background: #1f3d8f; }
  .badge-round.alt { background: #e8a91c; }
  .badge-wide { width: 52px; height: 28px; border-radius: 6px; background: #6ab0e0; }
  .sponsor { font-size: 7px; color: #555; line-height: 1.3; }
  .sponsor strong { display: block; font-size: 10px; font-weight: 600; color: #7a2b7c; }
  .footer-line {
    position: absolute; left: 0; width: 100%; top: 801px;
    text-align: center; color: var(--white);
    font-size: 10px; font-weight: 700; word-spacing: 1px;
  }
  .footer-line .sep { margin: 0 10px; }
</style>
</head>
<body>
  <article class="flyer">
    <header class="flyer-header">
      <div class="rule-top"></div>
      <div class="brand-box"><span class="brand-mark"></span><span class="brand-name">MV Linkway</span></div>
      <h1 class="headline-join"><span class="script">Join </span><span class="site">MVLinkway.org</span><span class="script"> today!</span></h1>
      <div class="photo photo-group" role="img" aria-label="Photo of a group of women standing together outdoors"></div>
      <div class="photo photo-beach" role="img" aria-label="Photo of two women walking on a rocky beach"></div>
      <div class="rule-band"></div>
    </header>

    <section class="info-panel">
      <div class="column column-left">
        <h2 class="section-title">Who Can Participate</h2>
        <ul class="audience-list">
          <li>Patients</li>
          <li>Family members</li>
          <li>Healthcare providers</li>
          <li>Investigators &amp; researchers</li>
          <li>All stakeholders interested in TRBQ</li>
        </ul>
        <h2 class="section-title">How it Works</h2>
        <p>Patients can join the registry to submit their data. After taking web-based surveys, explore the collected information in a way that protects the privacy of everyone.</p>
        <h2 class="section-title">Who We Are</h2>
        <p>As its name implies, MV Linkway represents the coming together of a wide range of entities and individuals who recognize the value in pooling their combined expertise and information. The Governing Board of MV Linkway comes from leaders in the non-profit sector, government agencies and academic institutions.</p>
        <p>Regardless of their individual backgrounds, the thought leaders of MV Linkway share a common goal to increase the community’s ability to help one another through improved communication, and by doing so, to help the millions of people affected by Lipodystrophy.</p>
      </div>
      <div class="column column-right">
        <h2 class="section-title large">Get Connected.</h2>
        <p>One of the most important steps towards finding effective treatments for lipodystrophy (LD) is to uncover the ways in which the diseases behave, the symptoms that are commonly seen and how those symptoms progress. This requires the collection of as much information as possible about all people affected by LD. MV Linkway will serve as that database–the critical link between the patient community and the scientific community. The more people who join the registry the greater the chances that research will produce results that benefit everyone.</p>
        <p>Join THE LINKWAY TRBQ Registry to:</p>
        <ul class="benefit-list">
          <li><svg width="10" height="10" viewBox="0 0 10 10"><path d="M1 5.5 L4 8.5 L9 1.5" fill="none" stroke="#d7141c" stroke-width="2"/></svg>Tell us about your experience with LD and learn about the experiences with others</li>
          <li><svg width="10" height="10" viewBox="0 0 10 10"><path d="M1 5.5 L4 8.5 L9 1.5" fill="none" stroke="#d7141c" stroke-width="2"/></svg>Share information in a program that protects your privacy</li>
          <li><svg width="10" height="10" viewBox="0 0 10 10"><path d="M1 5.5 L4 8.5 L9 1.5" fill="none" stroke="#d7141c" stroke-width="2"/></svg>Provide valuable quality-of-life information that can be used to advocate on behalf of the LD community</li>
          <li><svg width="10" height="10" viewBox="0 0 10 10"><path d="M1 5.5 L4 8.5 L9 1.5" fill="none" stroke="#d7141c" stroke-width="2"/></svg>Help the research community launch clinical trials and studies</li>
        </ul>
        <p>We need to hear YOUR VOICE and we hope you will decide to join MV Linkway. Every individual who joins makes a vital contribution toward helping all of those affected by lipodystrophy.</p>
      </div>
    </section>

    <p class="closing-line">Your information will lead to<br>future treatments and cures for all types of Lipodystrophy</p>

    <div class="partner-strip">
      <span class="partner-name"><span class="mark"></span>Allied Hope United</span>
      <span class="badge-round"></span>
      <span class="badge-round alt"></span>
      <span class="badge-wide"></span>
      <span class="sponsor">Sponsored by:<strong>Northvale Pharma</strong></span>
    </div>

    <footer class="footer-line">www.TRBQRegistry.org<span class="sep">|</span>info@carepathhub.com<span class="sep">|</span>Copyright © 2014 CarePath Hub</footer>
  </article>
</body>
</html>
```